New business card, letter head, email signature and Portfolio for our Security company.

We are an Vantage security company that provides a top quality manpower services to protect high rise buildings, retail and all type of properties and would like a new business card/logo look.

- We would like the spot UV design.
- Matt black (double sided).
- We would like to incorporate a royal blue colour (feel free to experiment with it).
- Feel free to try different lengths with the card to make it stand out more than a normal business card.
- We would like the logo to be an eagle eye in the background (shines when card is tilted slightly in the background, either on the front, back or both sides of the card). Image attached as an example of eye shape (colour to be either black or royal blue).
- MARLOW VANTAGE GUARD AGENCY PTY. LTD. and MVGA to be placed on one side of the card and on the other side of the card to have;

- Name in slightly bigger font than the position (directly on the bottom on the name).
- Mobile number
- Email address
- Website email address
- PO BOX address

Can we please have the files in a format that we can edit.

Reason: I need to consult my business partner with the designs so far and will make a decision from there.

Target Market(s)

Security Industry

Industry/Entity Type

Business

Contact Information for Business Card

- Mobile number
- Email address
- Website email address
- PO BOX address

Logo Text

MVGA and underneath the MVGA please add MARLOW VANTAGE GUARD AGENCY PTY. LTD.

Font styles to use
Other font styles liked:
• bold type font

Colors
0255a3
000000

Requirements
Must have
• We are an Vantage security company that provides a top quality manpower services to protect high rise buildings, retail and all type of properties and would like a new business card/logo look.
• - We would like the spot UV design.
• - Matt black (double sided).
• - We would like to incorporate a royal blue colour (feel free to experiment with it).
• - Feel free to try different lengths with the card to make it stand out more than a normal business card.
• - We would like the logo to be an eagle eye in the background (shines when card is tilted slightly in the background, either on the front, back or both sides of the card). Image attached as an example of eye shape (colour to be either black or royal blue).
• - MARLOW VANTAGE GUARD AGENCY PTY. LTD. and MVGA to be placed on one side of the card and on the other side of the card to have;
• - Name in slightly bigger font than the position (directly on the bottom on the name).
• - Mobile number
• - Email address
• - Website email address
• - PO BOX address
• Can we please have the files in a format that we can edit.
Nice to have
• Feel free to try different lengths with the card to make it stand out more than a normal business card.
• Please find "URBAN JUNGLE" font attached and incorporate MVGA into the same style with building's inside the MVGA bold front also add MARLOW into the bottom part of the S and follow on E - Vantage on the bottom S - SECURITY on the bottom S - SERVICES on the bottom of each letter.
• other than that, I'll be happy with a bold modern font for the MVGA and MARLOW VANTAGE GUARD AGENCY in a bold and thinner font underneath.

```html
<!DOCTYPE html>
<html lang="en">
<head>
<meta charset="utf-8">
<title>MVGA Business Card</title>
<link href="https://fonts.googleapis.com/css2?family=Roboto:wght@400;700&display=swap" rel="stylesheet">
<style>
  :root {
    --backdrop: #ece9e4;
    --royal-blue: #0a56a6;
    --royal-blue-deep: #084a8f;
    --card-black: #333333;
    --text-light: #dcdcdc;
    --text-white: #f2f2f2;
  }
  * { margin: 0; padding: 0; box-sizing: border-box; }
  html, body {
    width: 1200px; height: 400px; overflow: hidden;
    background: var(--backdrop);
    font-family: "Roboto", Arial, sans-serif;
  }
  .canvas { position: relative; width: 1200px; height: 400px; }
  .card {
    position: absolute; top: 93px; width: 479px; height: 213px;
  }
  .card--front { left: 109px; background: var(--royal-blue); }
  .card--back { left: 613px; background: var(--card-black); }

  .front-mark {
    position: absolute; left: 0; right: 0; top: 82px;
    text-align: center;
    font-weight: 700; font-size: 44px; letter-spacing: 2px;
    color: var(--royal-blue-deep);
  }

  .brand-dot {
    position: absolute; left: 70px; top: 58px;
    width: 84px; height: 84px; border-radius: 50%;
    background: var(--royal-blue);
  }
  .brand {
    position: absolute; left: 218px; top: 22px;
  }
  .brand__name {
    font-weight: 700; font-size: 58px; line-height: 64px;
    color: var(--text-white); letter-spacing: 1px;
  }
  .brand__tagline {
    font-weight: 700; font-size: 8.5px; letter-spacing: 0.4px;
    color: var(--text-white); margin-top: 1px;
  }

  .contact {
    position: absolute; left: 218px; top: 117px;
    color: var(--text-light);
  }
  .contact__name {
    font-weight: 700; font-size: 12px; color: var(--text-white);
    margin-bottom: 3px;
  }
  .contact__list { list-style: none; }
  .contact__item {
    display: flex; align-items: center;
    font-size: 12px; line-height: 16px; height: 16px;
  }
  .contact__icon { width: 9px; height: 9px; margin: 0 13px 0 4px; flex: none; }
  .contact__icon--blank { visibility: hidden; }
</style>
</head>
<body>
<main class="canvas">
  <section class="card card--front">
    <div class="front-mark">MVGA</div>
  </section>

  <section class="card card--back">
    <div class="brand-dot"></div>
    <div class="brand">
      <div class="brand__name">MVGA</div>
      <div class="brand__tagline">MARLOW VANTAGE GUARD AGENCY</div>
    </div>

    <div class="contact">
      <div class="contact__name">JORDAN REYES</div>
      <ul class="contact__list">
        <li class="contact__item">
          <svg class="contact__icon" viewBox="0 0 9 9"><rect width="9" height="9" fill="#0a56a6"/><rect x="3" y="1.5" width="3" height="6" rx="0.6" fill="#dcdcdc"/></svg>
          MOBILE NUMBER
        </li>
        <li class="contact__item">
          <svg class="contact__icon" viewBox="0 0 9 9"><rect width="9" height="9" fill="#0a56a6"/><rect x="1.5" y="2.5" width="6" height="4" fill="none" stroke="#dcdcdc" stroke-width="0.8"/><path d="M1.5 2.5 L4.5 5 L7.5 2.5" fill="none" stroke="#dcdcdc" stroke-width="0.8"/></svg>
          EMAIL ADDRESS
        </li>
        <li class="contact__item">
          <svg class="contact__icon" viewBox="0 0 9 9"><rect width="9" height="9" fill="#0a56a6"/><circle cx="4.5" cy="4.5" r="2.6" fill="none" stroke="#dcdcdc" stroke-width="0.8"/><path d="M1.9 4.5 H7.1 M4.5 1.9 V7.1" stroke="#dcdcdc" stroke-width="0.6"/></svg>
          WEBSITE EMAIL ADDRESS
        </li>
        <li class="contact__item">
          <svg class="contact__icon contact__icon--blank" viewBox="0 0 9 9"></svg>
          PO BOX ADDRESS
        </li>
      </ul>
    </div>
  </section>
</main>
</body>
</html>
```